Digital Album Cover - Vellorin Tamsuvel Under Copper Skies (Piano & Cello)

Hi
I would like a digital album cover

Title: "Under Copper Skies (Piano & Cello)"
Artist: "Caleb Rourke & The Pell Orsola"

Preview of instrumental song:
https://tunevault-example.net/calebrourkepianist/tamsuvel-under-copper-skies-piano-and-cello

```html
<!DOCTYPE html>
<html lang="en">
<head>
<meta charset="utf-8">
<title>Under Copper Skies – Album Cover and Disc</title>
<link rel="stylesheet" href="https://fonts.googleapis.com/css2?family=Kaushan+Script&family=Yesteryear&family=Libre+Baskerville&family=Lexend:wght@300&display=swap">
<style>
  :root {
    --stage-gold: #d1a54b;
    --navy-deep: #0f1d3a;
    --navy-mid: #173058;
    --title-gold: #d8b04a;
    --accent-gold: #d9a944;
    --label-white: #f2f2f2;
    --sky-top: #27406a;
    --sky-low: #6f93b3;
    --earth-warm: #b5704a;
    --snow: #e9eef2;
  }
  * { margin: 0; padding: 0; box-sizing: border-box; }
  html, body {
    width: 1200px; height: 778px; overflow: hidden;
    background: var(--stage-gold);
  }
  .stage { position: relative; width: 1200px; height: 778px; }
  .disc { position: absolute; left: 608px; top: 103px; width: 534px; height: 534px; }
  .album-cover { position: absolute; left: 65px; top: 78px; width: 584px; height: 584px; }
  .caption {
    position: absolute; top: 684px; width: 300px; text-align: center;
    font-family: "Lexend", sans-serif; font-weight: 300; font-size: 21px;
    letter-spacing: 1px; color: var(--label-white);
  }
  .caption--cover { left: 207px; }
  .caption--disc { left: 725px; }
  .title-text { font-family: "Kaushan Script", cursive; fill: var(--title-gold); }
  .artist-name { font-family: "Yesteryear", cursive; fill: var(--accent-gold); }
  .meta-label { font-family: "Libre Baskerville", serif; fill: var(--label-white); }
  .icon-ring { fill: none; stroke: var(--accent-gold); stroke-dasharray: 4 3; }
  .artist-rule { stroke: var(--accent-gold); stroke-dasharray: 6 4; }
  .icon-glyph { fill: var(--label-white); }
</style>
</head>
<body>
<main class="stage">

  <svg class="disc" viewBox="0 0 534 534" aria-label="Disc label: Under Copper Skies">
    <defs>
      <clipPath id="disc-shape"><circle cx="267" cy="267" r="267"/></clipPath>
      <mask id="spindle-mask">
        <rect width="534" height="534" fill="#fff"/>
        <circle cx="268" cy="271" r="66" fill="#000"/>
      </mask>
      <linearGradient id="disc-bg" x1="0" y1="0" x2="0" y2="1">
        <stop offset="0" stop-color="var(--navy-deep)"/>
        <stop offset="0.5" stop-color="var(--navy-mid)"/>
        <stop offset="1" stop-color="var(--navy-deep)"/>
      </linearGradient>
      <linearGradient id="disc-landscape" x1="0" y1="0" x2="0" y2="1">
        <stop offset="0" stop-color="var(--sky-top)"/>
        <stop offset="0.45" stop-color="var(--sky-low)"/>
        <stop offset="0.7" stop-color="var(--snow)"/>
        <stop offset="0.85" stop-color="var(--earth-warm)"/>
        <stop offset="1" stop-color="#5f7f95"/>
      </linearGradient>
      <radialGradient id="disc-nebula" cx="0.5" cy="0.4" r="0.6">
        <stop offset="0" stop-color="#3b4566"/>
        <stop offset="1" stop-color="#1a2442"/>
      </radialGradient>
      <linearGradient id="disc-planet" x1="0" y1="0" x2="0" y2="1">
        <stop offset="0" stop-color="#2c3c66"/>
        <stop offset="1" stop-color="#7a4a5e"/>
      </linearGradient>
    </defs>
    <g clip-path="url(#disc-shape)" mask="url(#spindle-mask)">
      <rect width="534" height="534" fill="url(#disc-bg)"/>
      <path role="img" aria-label="Starry nebula sky" fill="url(#disc-nebula)"
        d="M150,70 C145,40 185,28 215,32 C250,36 262,65 255,95 C245,130 190,150 140,180 C100,205 72,225 60,240 C75,200 120,160 150,70 Z"/>
      <path role="img" aria-label="Reddish planet surface at dusk" fill="url(#disc-planet)"
        d="M339,232 C355,190 380,158 415,157 C450,157 470,200 488,232 Z"/>
      <path role="img" aria-label="Starlit sky over snowy mountains and a lake" fill="url(#disc-landscape)"
        d="M0,257 L40,257 C80,300 160,310 215,300 C270,290 300,262 345,262 C405,262 470,257 534,257 L534,534 L300,534 C310,510 335,492 365,482 C300,465 250,430 200,390 C140,345 60,330 0,290 Z"/>
      <path fill="url(#disc-planet)" d="M300,262 C330,300 410,305 470,258 L300,258 Z"/>

      <g transform="rotate(-14 260 130)">
        <text class="title-text" x="85" y="122" font-size="40">Under Copper</text>
        <text class="title-text" x="250" y="180" font-size="56">Skies</text>
      </g>

      <g class="instrument piano">
        <circle class="icon-ring" cx="148" cy="409" r="16" stroke-width="1"/>
        <rect class="icon-glyph" x="140" y="402" width="16" height="13" rx="1.5"/>
        <g fill="var(--navy-deep)">
          <rect x="143" y="404" width="1.6" height="6"/><rect x="147" y="404" width="1.6" height="6"/>
          <rect x="151" y="404" width="1.6" height="6"/>
        </g>
        <text class="meta-label" x="148" y="438" font-size="8" text-anchor="middle">Piano</text>
      </g>
      <g class="instrument cello">
        <circle class="icon-ring" cx="193" cy="409" r="16" stroke-width="1"/>
        <g class="icon-glyph" transform="rotate(40 193 409)">
          <ellipse cx="193" cy="414" rx="4" ry="5.5"/>
          <ellipse cx="193" cy="407" rx="3" ry="3.5"/>
          <rect x="192.3" y="398" width="1.4" height="10"/>
        </g>
        <text class="meta-label" x="193" y="438" font-size="8" text-anchor="middle">Cello</text>
      </g>
      <text class="meta-label" x="138" y="464" font-size="8">Artist</text>
      <line class="artist-rule" x1="166" y1="461" x2="314" y2="461" stroke-width="0.8"/>
      <text class="artist-name" x="138" y="486" font-size="16" textLength="177" lengthAdjust="spacingAndGlyphs">Caleb Rourke &amp; The Pell Orsola</text>
    </g>
  </svg>

  <svg class="album-cover" viewBox="0 0 584 584" aria-label="Album cover: Under Copper Skies">
    <defs>
      <linearGradient id="cover-bg" x1="0" y1="0" x2="0" y2="1">
        <stop offset="0" stop-color="var(--navy-deep)"/>
        <stop offset="0.5" stop-color="var(--navy-mid)"/>
        <stop offset="1" stop-color="var(--navy-deep)"/>
      </linearGradient>
      <linearGradient id="landscape" x1="0" y1="0" x2="0" y2="1">
        <stop offset="0" stop-color="var(--sky-top)"/>
        <stop offset="0.45" stop-color="var(--sky-low)"/>
        <stop offset="0.7" stop-color="var(--snow)"/>
        <stop offset="0.85" stop-color="var(--earth-warm)"/>
        <stop offset="1" stop-color="#5f7f95"/>
      </linearGradient>
      <radialGradient id="nebula" cx="0.5" cy="0.5" r="0.6">
        <stop offset="0" stop-color="#3b4566"/>
        <stop offset="1" stop-color="#1a2442"/>
      </radialGradient>
      <linearGradient id="planet" x1="0" y1="0" x2="0" y2="1">
        <stop offset="0" stop-color="#2c3c66"/>
        <stop offset="1" stop-color="#7a4a5e"/>
      </linearGradient>
    </defs>
    <rect width="584" height="584" fill="url(#cover-bg)"/>
    <g class="artwork-windows">
      <path role="img" aria-label="Starry nebula sky" fill="url(#nebula)"
        d="M120,120 C110,60 150,25 205,26 C260,28 290,60 285,95 C280,130 220,140 150,175 C100,200 70,215 50,220 C80,190 130,160 120,120 Z"/>
      <path role="img" aria-label="Reddish planet surface at dusk" fill="url(#planet)"
        d="M420,254 C430,200 450,170 485,168 C520,168 535,210 545,254 Z"/>
      <path role="img" aria-label="Starlit sky over snowy mountains and a lake" fill="url(#landscape)"
        d="M32,282 L75,282 C120,330 210,340 270,325 C330,312 370,285 420,285 C470,285 510,282 584,282 L584,584 L346,584 C356,555 390,535 425,522 C360,505 300,470 245,430 C180,385 90,350 32,282 Z"/>
      <path fill="url(#planet)" d="M330,300 C360,330 420,330 480,285 L330,285 Z"/>
    </g>

    <g transform="rotate(-14 300 220)">
      <text class="title-text" x="60" y="222" font-size="56">Under Copper</text>
      <text class="title-text" x="210" y="320" font-size="80">Skies</text>
    </g>

    <g class="instrument piano">
      <circle class="icon-ring" cx="62" cy="431" r="24" stroke-width="1.3"/>
      <rect class="icon-glyph" x="50" y="420" width="24" height="20" rx="2"/>
      <g fill="var(--navy-deep)">
        <rect x="55" y="423" width="2.5" height="9"/><rect x="60.5" y="423" width="2.5" height="9"/>
        <rect x="66" y="423" width="2.5" height="9"/><rect x="53" y="434" width="18" height="1"/>
      </g>
      <text class="meta-label" x="62" y="474" font-size="12" text-anchor="middle">Piano</text>
    </g>
    <g class="instrument cello">
      <circle class="icon-ring" cx="129" cy="431" r="24" stroke-width="1.3"/>
      <g class="icon-glyph" transform="rotate(40 129 431)">
        <ellipse cx="129" cy="438" rx="6" ry="8"/>
        <ellipse cx="129" cy="428" rx="4.5" ry="5"/>
        <rect x="128" y="414" width="2" height="14"/>
      </g>
      <text class="meta-label" x="129" y="474" font-size="12" text-anchor="middle">Cello</text>
    </g>

    <text class="meta-label" x="47" y="518" font-size="12">Artist</text>
    <line class="artist-rule" x1="88" y1="514" x2="312" y2="514" stroke-width="1"/>
    <text class="artist-name" x="47" y="548" font-size="24" textLength="266" lengthAdjust="spacingAndGlyphs">Caleb Rourke &amp; The Pell Orsola</text>
  </svg>

  <p class="caption caption--cover">CD Cover Design</p>
  <p class="caption caption--disc">CD Design</p>
</main>
</body>
</html>
```